Bright Acorns Business Card Design

Bright Acorns - Cultivating Natural Play Spaces

Bright Acorns is a company that focuses on promoting the design, construction, consultation and support of natural, creative and organic play spaces for Early Childhood and learning environments.

We need a professional Business Card designed that is unique modern and creative. The Philosophy of the company is nostalgic so the business and will need to reflect this but also reflect that our ideas are modern and cutting edge.

The business card will need to be a talking point, by either having a unique size, quality and/or placement of logo or other quality.

I am more interested in using natural recycled paper, as this would reflect the philosophy of the company, but I open to seeing colour used creatively.
Updates

Hi Designers, Apologies, Could you please add www.brightacorns.com.au to the business card. Thanks very much.

Hi All, Thank you all for your submission thus far. Please note the fonts for used in the logo are: Ostrich Sans Black and Archer Semi Bold. If these could be considered for contact details, my name etc. Also please show the design on a recycled brown card if possible as this will be the type of card I will use when printing. Thanks so much.

Target Market(s)

Child Care Providers, Play Industry Professionals

Industry/Entity Type

Business

Contact Information for Business Card

Bright Acorns
Cultivating Natural Play Spaces
Marlene Okafor
0419 862 304
marlene@brightacorns.com.au

Font styles to use
Sans Serif

Requirements
Must have
• The Logo and the Details plus the below phrase
• Bright Acorns - Cultivating Natural Play Spaces
Nice to have
• A bit of colour, but not too much colour.
Should not have
• Not to have a white background, recycled brown card only

```html
<!DOCTYPE html>
<html lang="en">
<head>
<meta charset="utf-8">
<title>Bright Acorns Business Card Design</title>
<link rel="stylesheet" href="https://fonts.googleapis.com/css2?family=Arvo:wght@400;700&display=swap">
<style>
  :root {
    --backdrop: #e8e4de;
    --card: #c4a27a;
    --ink: #1f1812;
    --flourish: #8a6c4b;
    --card-shadow: rgba(0, 0, 0, 0.22);
  }
  * { margin: 0; padding: 0; box-sizing: border-box; }
  html, body {
    width: 1200px;
    height: 1000px;
    overflow: hidden;
  }
  body {
    position: relative;
    background: var(--backdrop);
    font-family: "Arvo", Georgia, serif;
    color: var(--ink);
  }
  .card {
    position: absolute;
    left: 237px;
    width: 726px;
    background: var(--card);
    border-radius: 40px;
    box-shadow: 0 4px 14px var(--card-shadow);
    text-align: center;
  }
  .card--front { top: 72px; height: 416px; }
  .card--back  { top: 513px; height: 414px; }

  /* front */
  .brand-mark {
    position: absolute;
    left: 318px;
    top: 72px;
    width: 90px;
    height: 90px;
    border-radius: 50%;
    background: var(--ink);
  }
  .est {
    position: absolute;
    left: 0; right: 0;
    top: 196px;
    font-size: 19px;
    letter-spacing: 1px;
    word-spacing: 60px;
  }
  .brand-name {
    position: absolute;
    left: 0; right: 0;
    top: 228px;
    font-size: 42px;
    font-weight: 700;
    letter-spacing: 1px;
    text-transform: uppercase;
  }
  .tagline {
    position: absolute;
    left: 0; right: 0;
    top: 290px;
    font-size: 16px;
    line-height: 20px;
    letter-spacing: 0.6px;
    text-transform: uppercase;
  }
  .flourish {
    position: absolute;
    left: 313px;
    top: 336px;
    width: 100px;
    height: 10px;
    border-radius: 5px;
    background: var(--flourish);
  }

  /* back */
  .brand-mark--small {
    position: absolute;
    left: 325px;
    top: 86px;
    width: 76px;
    height: 76px;
    border-radius: 50%;
    background: var(--ink);
  }
  .person-name {
    position: absolute;
    left: 0; right: 0;
    top: 193px;
    font-size: 21px;
    font-weight: 700;
    letter-spacing: 2px;
    text-transform: uppercase;
  }
  .name-rule {
    position: absolute;
    left: 333px;
    top: 229px;
    width: 60px;
    height: 2px;
    background: var(--ink);
  }
  .contact-list {
    position: absolute;
    left: 0; right: 0;
    top: 250px;
    list-style: none;
    font-size: 17px;
    line-height: 28px;
  }
</style>
</head>
<body>
  <section class="card card--front">
    <div class="brand-mark" aria-hidden="true"></div>
    <p class="est">EST 2015</p>
    <h1 class="brand-name">Bright Acorns</h1>
    <p class="tagline">Cultivating<br>Natural Play Spaces</p>
    <div class="flourish" role="img" aria-label="Decorative swirl flourish"></div>
  </section>

  <section class="card card--back">
    <div class="brand-mark--small" aria-hidden="true"></div>
    <h2 class="person-name">Marlene Okafor</h2>
    <div class="name-rule"></div>
    <ul class="contact-list">
      <li>0419 862 304</li>
      <li>marlene@brightacorns.com.au</li>
      <li>www.brightacorns.com.au</li>
    </ul>
  </section>
</body>
</html>
```